Commercial and Multifamily informational website

We need a website for our commercial real estate management company. We will manage offices, retail, apartments and others. Here is the brief verbiage: Providing quality commercial and multifamily portfolio management to Landlords, REITs, and financial institutions. 

Industry/Entity Type

Real Estate

Number of Pages Required

2 page

Font styles to use
Sans Serif
Other font styles liked:
• Muli, Garamond

Colors
0555a3
5c5c5c
3176b5
85acd3
474747

Requirements
Must have
• Home page and contact page

```html
<!DOCTYPE html>
<html lang="en">
<head>
<meta charset="utf-8">
<title>Alder Real Estate Management</title>
<link href="https://fonts.googleapis.com/css2?family=Montserrat:wght@400;500;600&family=Lato:wght@400;700&family=Source+Sans+3:wght@600;700&display=swap" rel="stylesheet">
<style>
  :root{
    --blue:#0555a3;
    --blue-mid:#3176b5;
    --blue-light:#85acd3;
    --navy:#1c3f8a;
    --grey:#5c5c5c;
    --grey-dark:#474747;
    --line:#e6e6e6;
    --white:#ffffff;
  }
  *{box-sizing:border-box;margin:0;padding:0}
  html,body{width:876px;height:1200px;overflow:hidden;background:var(--white)}
  body{font-family:'Lato',sans-serif;color:var(--grey)}
  .page{position:relative;width:876px;height:1200px;overflow:hidden}
  .abs{position:absolute}

  /* hero */
  .hero-bg{left:0;top:0;width:876px;height:440px}
  .main-nav{left:231px;top:37px;width:414px;height:65px;display:flex}
  .main-nav a{flex:1;display:flex;align-items:center;justify-content:center;white-space:nowrap;
    font-family:'Montserrat',sans-serif;font-weight:600;font-size:7.6px;color:var(--white);
    text-decoration:none;padding-top:12px;background:var(--blue)}
  .main-nav a + a{border-left:1px solid rgba(255,255,255,.25)}
  .main-nav a.nav-search{background:var(--blue-mid)}
  .hero-card{left:230px;top:202px;width:415px;height:139px;background:rgba(255,255,255,.86);text-align:center}
  .hero-brand{margin-top:26px;font-family:'Montserrat',sans-serif;font-weight:600;color:var(--navy);
    font-size:19px;line-height:21px;letter-spacing:.5px}
  .hero-text{margin:14px auto 0;width:260px;font-size:5.4px;line-height:10px;color:#222}
  .btn-quote{left:390px;top:368px;width:95px;height:22px;background:var(--blue);color:var(--white);
    font-family:'Montserrat',sans-serif;font-size:6px;font-weight:600;display:flex;align-items:center;justify-content:center}
  .slide-next{left:803px;top:221px;width:19px;height:19px;background:var(--blue)}
  .home-badge{left:423px;top:416px;width:28px;height:28px;border-radius:50%;background:var(--white);
    box-shadow:0 1px 3px rgba(0,0,0,.15)}

  /* services */
  .service{top:505px;width:134px;text-align:center}
  .service-icon{display:block;margin:0 auto;width:32px;height:32px}
  .service-title{margin-top:16px;height:9px;line-height:9px;white-space:nowrap;font-family:'Montserrat',sans-serif;
    font-size:7px;letter-spacing:1.1px;color:var(--grey-dark)}
  .service-title.is-active{color:var(--navy);font-weight:600}
  .service-rule{width:16px;height:1px;background:#999;margin:6px auto 0}
  .service-text{margin:8px auto 0;width:106px;font-size:5px;line-height:8.4px;color:#8a8a8a}
  .btn-outline{display:block;margin:9px auto 0;width:62px;height:15px;border:1px solid #999;
    font-size:5.2px;line-height:13px;color:var(--grey)}
  .divider{left:34px;top:641px;width:809px;height:1px;background:var(--line)}

  /* welcome */
  .welcome-photo{left:191px;top:702px;width:233px;height:170px;
    background:linear-gradient(135deg,#c9c3bc 0%,#e9e6e1 45%,#8aa2bf 75%,#6f6f75 100%)}
  .welcome-photo::after{content:"";position:absolute;left:0;bottom:0;width:100%;height:15px;background:#2f3338}
  .welcome-head{left:438px;top:702px;border-left:2px solid var(--blue);padding-left:13px;
    font-family:'Source Sans 3',sans-serif;font-weight:700;font-size:14px;line-height:15px;letter-spacing:2.4px}
  .welcome-head span{display:block;color:var(--grey-dark)}
  .welcome-head strong{display:block;color:var(--navy)}
  .welcome-copy{left:438px;top:742px;width:250px;font-size:5.2px;line-height:12.3px;color:#8a8a8a}
  .welcome-copy p + p{margin-top:12px}
  .btn-solid{left:438px;top:849px;width:95px;height:23px;background:var(--blue);color:var(--white);
    font-family:'Montserrat',sans-serif;font-weight:600;font-size:7px;display:flex;align-items:center;justify-content:center}

  /* footer */
  .footer-photo{left:34px;top:942px;width:809px;height:202px;
    background:linear-gradient(90deg,#e4e4e4 0%,#c8cdd3 30%,#f2f2f2 50%,#c6ccd3 72%,#e8e8e8 100%)}
  .footer-info{left:34px;top:990px;width:809px;text-align:center}
  .footer-brand{font-family:'Montserrat',sans-serif;font-weight:600;color:var(--navy);font-size:17px;line-height:19px;letter-spacing:.5px}
  .footer-label{margin-top:20px;font-family:'Montserrat',sans-serif;font-size:7.2px;color:var(--blue)}
  .footer-address{margin-top:6px;font-family:'Montserrat',sans-serif;font-size:7.2px;color:var(--blue)}
  .footer-bar{left:34px;top:1144px;width:809px;height:38px;background:var(--grey-dark)}
  .social{left:191px;top:1160px;display:flex;gap:9px}
  .social span{width:7px;height:7px;border-radius:50%;background:#9a9a9a}
  .copyright{left:534px;top:1159px;width:200px;text-align:right;font-size:5px;color:#cfcfcf}
  .to-top{left:799px;top:1133px;width:22px;height:22px;border-radius:50%;background:var(--blue)}
</style>
</head>
<body>
<div class="page">

  <svg class="abs hero-bg" viewBox="0 0 876 440" role="img" aria-label="Photo of a suburban family house under a blue sky with lawn and flowering shrubs">
    <defs>
      <linearGradient id="heroSky" x1="0" y1="0" x2="0" y2="1">
        <stop offset="0" stop-color="#4f95d8"/>
        <stop offset="0.35" stop-color="#bcd3ea"/>
        <stop offset="0.62" stop-color="#c9c2bb"/>
        <stop offset="0.82" stop-color="#7d9a4c"/>
        <stop offset="1" stop-color="#4b7a2c"/>
      </linearGradient>
    </defs>
    <polygon points="34,37 843,37 843,382 437,428 34,382" fill="url(#heroSky)"/>
  </svg>

  <nav class="abs main-nav">
    <a href="#">HOME</a>
    <a href="#">CONTACT US</a>
    <a href="#" class="nav-search">SEARCH ALDER PROPERTIES</a>
  </nav>

  <svg class="abs" style="left:58px;top:224px" width="10" height="12" viewBox="0 0 10 12"><path d="M7 1 2 6l5 5" fill="none" stroke="#ffffff" stroke-width="1.3" opacity=".8"/></svg>
  <svg class="abs slide-next" viewBox="0 0 19 19"><path d="M8 5l4.5 4.5L8 14" fill="none" stroke="#ffffff" stroke-width="1.5"/></svg>

  <div class="abs hero-card">
    <div class="hero-brand">ALDER<br>REAL ESTATE MANAGEMENT</div>
    <p class="hero-text">Lorem Ipsum is simply dummy text of the printing and typesetting industry. Lorem Ipsum has been the industry's standard dummy text ever since the 1500s, when an unknown printer took a galley of type and scrambled it to make a type specimen book.</p>
  </div>
  <a class="abs btn-quote">GET A QUOTE</a>

  <div class="abs home-badge">
    <svg width="28" height="28" viewBox="0 0 28 28"><path d="M14 7 6.5 13.5h2V20h4v-4h3v4h4v-6.5h2z" fill="#0555a3"/></svg>
  </div>

  <section>
    <div class="abs service" style="left:178px">
      <svg class="service-icon" viewBox="0 0 32 32"><rect x="6" y="6" width="20" height="20" transform="rotate(45 16 16)" fill="none" stroke="#0555a3" stroke-width=".8"/><circle cx="16" cy="15" r="3" fill="none" stroke="#0555a3" stroke-width=".8"/><path d="M15 18.5v1.5h2v-1.5" fill="none" stroke="#0555a3" stroke-width=".8"/></svg>
      <div class="service-title is-active">MANAGEMENT SERVICES</div>
      <div class="service-rule"></div>
      <p class="service-text">Lorem Ipsum is simply dummy text of the printing and typesetting let. Lorem Ipsum has been the industry.</p>
      <span class="btn-outline">LEARN MORE</span>
    </div>
    <div class="abs service" style="left:310px">
      <svg class="service-icon" viewBox="0 0 32 32"><rect x="1" y="1" width="30" height="30" fill="none" stroke="#dddddd" stroke-width=".8"/><path d="M16 9a4 4 0 0 1 4 4c0 3-4 7-4 7s-4-4-4-7a4 4 0 0 1 4-4z" fill="none" stroke="#3176b5" stroke-width=".8"/><ellipse cx="16" cy="21" rx="6" ry="2" fill="none" stroke="#3176b5" stroke-width=".8"/></svg>
      <div class="service-title">SEARCH RENTALS</div>
      <div class="service-rule"></div>
      <p class="service-text">Lorem Ipsum is simply dummy text of the printing and typesetting let. Lorem Ipsum has been the industry.</p>
      <span class="btn-outline">LEARN MORE</span>
    </div>
    <div class="abs service" style="left:436px">
      <svg class="service-icon" viewBox="0 0 32 32"><rect x="1" y="1" width="30" height="30" fill="none" stroke="#dddddd" stroke-width=".8"/><circle cx="19" cy="13" r="3" fill="none" stroke="#3176b5" stroke-width=".8"/><path d="M17 15l-6 6m2-2 1.5 1.5" fill="none" stroke="#3176b5" stroke-width=".8"/></svg>
      <div class="service-title">PROPERTY OWNERS</div>
      <div class="service-rule"></div>
      <p class="service-text">Lorem Ipsum is simply dummy text of the printing and typesetting let. Lorem Ipsum has been the industry.</p>
      <span class="btn-outline">LEARN MORE</span>
    </div>
    <div class="abs service" style="left:563px">
      <svg class="service-icon" viewBox="0 0 32 32"><rect x="1" y="1" width="30" height="30" fill="none" stroke="#dddddd" stroke-width=".8"/><rect x="12" y="12" width="6" height="6" fill="none" stroke="#3176b5" stroke-width=".8"/><rect x="14" y="14" width="6" height="6" fill="none" stroke="#3176b5" stroke-width=".8"/></svg>
      <div class="service-title">OFFICE SPACES</div>
      <div class="service-rule"></div>
      <p class="service-text">Lorem Ipsum is simply dummy text of the printing and typesetting let. Lorem Ipsum has been the industry.</p>
      <span class="btn-outline">LEARN MORE</span>
    </div>
  </section>

  <div class="abs divider"></div>

  <section>
    <div class="abs welcome-photo" role="img" aria-label="Photo of a smiling couple shaking hands with an agent across an office desk"></div>
    <h2 class="abs welcome-head"><span>WELCOME TO</span><strong>ALDER REAL ESTATE MANAGEMENT</strong></h2>
    <div class="abs welcome-copy">
      <p>Alder Real Estate Management is a sit amet, consectetuer adipiscing elit. Aenean commodo ligula eget dolor. Aenean massa. Cum sociis natoque penatibus et magnis dis parturient montes, nascetur ridiculus mus. Donec quam felis, ultricies nec, pellentesque eu, pretium quis, sem.</p>
      <p>It has survived not only five centuries, but also the leap into electronic typesetting, remaining essentially unchanged. It was popularised in the 1960s with the release of Typeline sheets containing Lorem Ipsum passages, and more recently with desktop publishing software like Quillpress Layout including versions of Lorem Ipsum.</p>
    </div>
    <a class="abs btn-solid">LEARN MORE</a>
  </section>

  <footer>
    <div class="abs footer-photo" role="img" aria-label="Faded photo of hands passing house keys and a small paper house cutout"></div>
    <div class="abs footer-info">
      <div class="footer-brand">ALDER<br>REAL ESTATE MANAGEMENT</div>
      <p class="footer-label">Office Address:</p>
      <p class="footer-address">Lorem Ipsum is simply dummy text of the printing and typesetting</p>
    </div>
    <div class="abs footer-bar"></div>
    <div class="abs social"><span></span><span></span><span></span><span></span></div>
    <p class="abs copyright">Alder Real Estate Management © 2017 All Rights Reserved</p>
    <div class="abs to-top">
      <svg width="22" height="22" viewBox="0 0 22 22"><path d="M8 12.5l3-3 3 3" fill="none" stroke="#ffffff" stroke-width="1.2"/></svg>
    </div>
  </footer>

</div>
</body>
</html>
```